Looking for potential sellers

We help people buy and sell homes and are currently looking for potential home sellers. We offer low commissions, are the Local Colorado Springs and Falcon Experts, homes selling fast and at top dollar, Free expert pricing opinions and Consultations, over 9 years of experience, top rated Realtors creative and aggressive marketing strategies. Don't just tour the town, ROAM Kestrelby. phone number 555-013-8842 web roamkestrelby.example

```html
<!DOCTYPE html>
<html lang="en">
<head>
<meta charset="utf-8">
<title>Meridian Hearth Realty – Seller Postcard</title>
<link rel="stylesheet" href="https://fonts.googleapis.com/css2?family=Gabriela&family=Montserrat:wght@800&family=Oswald:wght@500&family=Lato:ital,wght@0,400;0,700;0,900;1,700;1,900&family=Poppins:wght@600;700&display=swap">
<style>
  :root {
    --page: #e4e4e4;
    --ink: #1c1c1c;
    --charcoal: #262626;
    --olive: #8e8f27;
    --olive-deep: #6f701c;
    --olive-light: #d9dc66;
    --lime-text: #c9cf52;
    --red: #e1262c;
    --white: #ffffff;
  }
  * { box-sizing: border-box; margin: 0; padding: 0; }
  html, body { width: 902px; height: 1200px; overflow: hidden; }
  body { background: var(--page); font-family: "Lato", sans-serif; position: relative; }

  .postcard { position: absolute; width: 754px; height: 510px; overflow: hidden; box-shadow: 0 4px 14px rgba(0,0,0,.25); }
  .postcard--front { left: 46px; top: 58px; background: var(--charcoal); }
  .postcard--back { left: 83px; top: 633px; width: 755px; background: var(--white); }
  .postcard > svg.shapes { position: absolute; inset: 0; }
  .abs { position: absolute; }

  /* front */
  .headline__lead { left: 34px; top: 22px; font-family: "Gabriela", serif; font-size: 27px; color: var(--lime-text); white-space: nowrap; }
  .headline__main { left: 33px; top: 58px; font-family: "Montserrat", sans-serif; font-weight: 800; font-size: 40px; color: var(--white); letter-spacing: .5px; white-space: nowrap; }
  .agent-photo { left: 24px; top: 104px; width: 240px; height: 274px; background: linear-gradient(160deg, #c7c7c7, #8c8f97 55%, #5b5f6b); }
  .brand { display: flex; align-items: center; gap: 7px; font-family: "Lato", sans-serif; font-weight: 700; color: var(--ink); white-space: nowrap; }
  .brand__mark { width: 12px; height: 12px; background: var(--olive); flex: none; }
  .brand--front { left: 200px; top: 172px; font-size: 15px; }
  .agent-name { left: 50px; top: 383px; font-weight: 700; font-size: 15px; color: var(--white); white-space: nowrap; }
  .agent-name b, .agent-name--back b { color: var(--olive-light); }
  .offer-badge { left: 270px; top: 282px; width: 122px; height: 122px; }
  .offer-badge__text { position: absolute; inset: 0; display: flex; flex-direction: column; align-items: center; justify-content: center; transform: rotate(-24deg); font-family: "Montserrat", sans-serif; font-weight: 800; color: var(--white); font-size: 22px; line-height: 1.05; }
  .hero-photo { left: 0; top: 0; width: 754px; height: 212px; clip-path: polygon(455px 0, 754px 0, 754px 212px, 425px 212px); background: linear-gradient(180deg, #6f9ad0 0%, #c9d8ea 45%, #e9e4d6 62%, #6c8a45 100%); }
  .promise { left: 410px; top: 220px; font-family: "Oswald", sans-serif; font-weight: 500; font-size: 20px; color: var(--ink); white-space: nowrap; }
  .promise span { color: var(--white); }
  .benefits { left: 410px; top: 266px; list-style: none; color: var(--white); font-size: 10.5px; }
  .benefits li { display: flex; align-items: center; gap: 8px; height: 19px; }
  .benefits li::before { content: ""; width: 7px; height: 7px; border-radius: 50%; background: var(--white); }
  .commission { left: 412px; top: 329px; width: 293px; height: 42px; border-radius: 21px; background: linear-gradient(180deg, #f1f3a6, #b8ba3c); box-shadow: 0 2px 4px rgba(0,0,0,.5); }
  .commission__icon { position: absolute; left: 4px; top: 3px; width: 36px; height: 36px; }
  .commission__label { position: absolute; left: 70px; top: 5px; font-style: italic; font-weight: 900; font-size: 23px; color: var(--ink); white-space: nowrap; }
  .experience { left: 437px; top: 381px; font-style: italic; font-weight: 700; font-size: 19px; color: var(--charcoal); white-space: nowrap; }
  .tagline { left: 27px; top: 424px; font-family: "Poppins", sans-serif; font-weight: 700; color: var(--ink); font-size: 14.5px; line-height: 1.25; white-space: nowrap; }
  .tagline strong { font-size: 21px; color: var(--white); }
  .contact__label { font-weight: 700; font-size: 14px; color: var(--ink); white-space: nowrap; }
  .contact__phone { display: flex; align-items: center; gap: 6px; font-family: "Poppins", sans-serif; font-weight: 700; color: var(--ink); white-space: nowrap; }
  .contact__phone svg { flex: none; }
  .contact--front { left: 262px; top: 426px; }
  .contact--front .contact__phone { font-size: 25px; margin-top: 2px; }
  .web { color: var(--white); white-space: nowrap; }
  .web__label { font-size: 11px; font-weight: 700; }
  .web__url { display: flex; align-items: center; gap: 4px; font-family: "Poppins", sans-serif; font-weight: 600; }
  .web__url::before { content: ""; width: 6px; height: 6px; border-radius: 50%; background: currentColor; }
  .web--front { left: 518px; top: 443px; }
  .web--front .web__url { font-size: 14px; }

  /* back */
  .landscape { left: 0; top: 0; width: 755px; height: 140px; clip-path: polygon(0 0, 412px 0, 400px 140px, 0 140px); background: linear-gradient(180deg, #a85d55 0%, #6f6f7a 35%, #d5d5d5 55%, #2d4a32 75%, #23372a 100%); }
  .brand--back { left: 215px; top: 100px; font-size: 12px; color: var(--white); }
  .brand--back .brand__mark { background: var(--olive-light); width: 10px; height: 10px; }
  .market-note { left: 20px; top: 146px; width: 350px; font-style: italic; font-weight: 700; font-size: 10.3px; line-height: 1.3; color: var(--ink); }
  .portrait { left: 0; top: 213px; width: 755px; height: 205px; clip-path: polygon(0 0, 393px 0, 375px 205px, 0 205px); background: linear-gradient(90deg, #8d7868 0%, #b49d88 50%, #8f7b6c 100%); }
  .portrait__face { position: absolute; left: 200px; top: 0; width: 150px; height: 205px; background: linear-gradient(180deg, #b88f76, #3b3a3f); border-radius: 70px 70px 0 0; opacity: .55; }
  .back-tagline { left: 22px; top: 248px; font-family: "Poppins", sans-serif; font-weight: 600; font-size: 12.5px; line-height: 1.3; color: var(--white); }
  .review { left: 22px; top: 294px; width: 188px; font-style: italic; font-weight: 700; font-size: 10.3px; line-height: 1.33; color: var(--white); text-align: justify; }
  .review__author { display: block; font-style: normal; margin-top: 8px; font-size: 11.5px; }
  .agent-name--back { left: 215px; top: 406px; font-weight: 700; font-size: 10.5px; color: var(--white); white-space: nowrap; }
  .contact--back { left: 20px; top: 433px; }
  .contact--back .contact__label { font-size: 11px; }
  .contact--back .contact__phone { font-size: 15px; margin-top: 4px; }
  .web--back { left: 164px; top: 435px; color: var(--white); }
  .web--back .web__label { font-size: 10px; }
  .web--back .web__url { font-size: 11.5px; margin-top: 5px; }
  .indicia { left: 628px; top: 35px; width: 90px; height: 82px; border: 1px solid #555; font-size: 11px; line-height: 1.3; text-align: center; padding-top: 6px; color: var(--ink); white-space: nowrap; }
  .indicia b { font-weight: 900; }
  .mail-panel { left: 495px; top: 332px; width: 226px; height: 92px; border: 1.5px solid #333; padding: 6px 12px; color: var(--ink); font-size: 10.5px; line-height: 1.3; }
  .mail-panel__route { text-align: right; letter-spacing: .3px; margin-bottom: 38px; }
</style>
</head>
<body>

<section class="postcard postcard--front" aria-label="Postcard front">
  <svg class="shapes" width="754" height="510" viewBox="0 0 754 510" aria-hidden="true">
    <defs>
      <linearGradient id="headerShade" x1="0" y1="0" x2="1" y2="0">
        <stop offset="0" stop-color="#0f0f0f"/><stop offset="1" stop-color="#4a4a4a"/>
      </linearGradient>
      <linearGradient id="panelShade" x1="0" y1="0" x2="1" y2="1">
        <stop offset="0" stop-color="#ffffff"/><stop offset="1" stop-color="#cfcfcf"/>
      </linearGradient>
      <linearGradient id="barShade" x1="0" y1="0" x2="1" y2="0">
        <stop offset="0" stop-color="#9c9d2f"/><stop offset="1" stop-color="#dcdf6a"/>
      </linearGradient>
      <linearGradient id="bandShade" x1="0" y1="0" x2="1" y2="0">
        <stop offset="0" stop-color="#8c8d25"/><stop offset=".42" stop-color="#a9aa33"/>
        <stop offset=".55" stop-color="#e6ea76"/><stop offset=".72" stop-color="#8f9028"/>
        <stop offset="1" stop-color="#7c7d1f"/>
      </linearGradient>
      <linearGradient id="swooshShade" x1="0" y1="0" x2="0" y2="1">
        <stop offset="0" stop-color="#ffffff"/><stop offset="1" stop-color="#c8c8c8"/>
      </linearGradient>
    </defs>
    <rect width="754" height="510" fill="#262626"/>
    <polygon points="0,112 420,112 392,380 0,380" fill="url(#panelShade)"/>
    <rect width="440" height="112" fill="url(#headerShade)"/>
    <polygon points="430,0 456,0 397,408 371,408" fill="var(--olive)"/>
    <polygon points="422,218 754,218 754,250 418,250" fill="url(#barShade)"/>
    <path d="M382 412 Q540 345 754 362 L754 412 Z" fill="url(#swooshShade)"/>
    <rect x="0" y="378" width="380" height="32" fill="#2b2b2b"/>
    <rect x="0" y="408" width="754" height="80" fill="url(#bandShade)"/>
    <line x1="255" y1="414" x2="255" y2="482" stroke="#6f701c" stroke-width="1"/>
    <line x1="509" y1="414" x2="509" y2="482" stroke="#6f701c" stroke-width="1"/>
    <rect x="0" y="484" width="754" height="4" fill="#ffffff"/>
  </svg>

  <div class="hero-photo abs" role="img" aria-label="Photo of a white two-storey house with a porch and a sold sign on the lawn"></div>

  <p class="headline__lead abs">Looking to Sell Your Home?</p>
  <h1 class="headline__main abs">WE SELL HOMES</h1>

  <div class="agent-photo abs" role="img" aria-label="Portrait of the agent in a plaid shirt"></div>
  <div class="brand brand--front abs"><span class="brand__mark"></span>Meridian Hearth Realty</div>
  <p class="agent-name abs">Dale Warren <b>AGENT</b></p>

  <div class="offer-badge abs">
    <svg width="122" height="122" viewBox="0 0 122 122" aria-hidden="true">
      <polygon fill="var(--red)" points="61,4 70,20 86,10 89,28 107,26 101,44 118,51 104,62 116,76 98,81 103,99 85,97 80,115 66,104 54,118 47,101 29,108 29,90 11,86 21,71 5,60 21,51 13,34 31,33 31,15 48,22"/>
    </svg>
    <div class="offer-badge__text"><span>WE</span><span>OFFER</span></div>
  </div>

  <p class="promise abs">HOMES SELLING FAST <span>AND AT TOP DOLLAR</span></p>
  <ul class="benefits abs">
    <li>The Local Colorado Springs and Falcon Experts</li>
    <li>Free expert pricing opinions and Consultations</li>
    <li>Top rated Realtors creative and aggressive marketing strategies</li>
  </ul>
  <div class="commission abs">
    <svg class="commission__icon" viewBox="0 0 36 36" aria-hidden="true">
      <circle cx="18" cy="18" r="17" fill="#a3a52e" stroke="#ffffff" stroke-width="1.5"/>
      <path d="M12 9 H24 V19 H28 L18 29 L8 19 H12 Z" fill="none" stroke="#1c1c1c" stroke-width="1.5" stroke-linejoin="round"/>
      <text x="18" y="21" font-family="Lato, sans-serif" font-weight="900" font-size="11" text-anchor="middle" fill="#1c1c1c">$</text>
    </svg>
    <span class="commission__label">Low commissions</span>
  </div>
  <p class="experience abs">Over 9 years of experience</p>

  <p class="tagline abs">Don't just tour the town,<br><strong>ROAM Kestrelby.</strong></p>
  <div class="contact contact--front abs">
    <p class="contact__label">Get in touch with us</p>
    <p class="contact__phone">
      <svg width="22" height="22" viewBox="0 0 24 24" aria-hidden="true"><circle cx="12" cy="12" r="10.5" fill="none" stroke="#1c1c1c" stroke-width="2"/><path d="M8.5 6.5 L10.5 6.5 L11.3 9.3 L10 10.4 Q11 12.8 13.6 14 L14.7 12.7 L17.5 13.5 L17.5 15.5 Q17 17.5 15 17.3 Q7 16 6.7 8.5 Q6.8 6.7 8.5 6.5 Z" fill="#1c1c1c"/></svg>
      555-013-8842
    </p>
  </div>
  <div class="web web--front abs">
    <p class="web__label">For more information visit Us on :</p>
    <p class="web__url">www.roamkestrelby.example</p>
  </div>
</section>

<section class="postcard postcard--back" aria-label="Postcard back">
  <svg class="shapes" width="755" height="510" viewBox="0 0 755 510" aria-hidden="true">
    <defs>
      <linearGradient id="noteShade" x1="0" y1="0" x2="1" y2="0">
        <stop offset="0" stop-color="#a2a334"/><stop offset="1" stop-color="#c3c54a"/>
      </linearGradient>
      <linearGradient id="footShade" x1="0" y1="0" x2="1" y2="0">
        <stop offset="0" stop-color="#e2e57a"/><stop offset=".42" stop-color="#c8ca50"/>
        <stop offset=".45" stop-color="#8d8e27"/><stop offset="1" stop-color="#7d7e20"/>
      </linearGradient>
    </defs>
    <polygon points="0,142 400,142 394,210 0,210" fill="url(#noteShade)"/>
    <polygon points="0,418 375,418 369,487 0,487" fill="url(#footShade)"/>
    <line x1="157" y1="426" x2="157" y2="480" stroke="#6f701c"/>
    <polygon points="412,0 428,0 343,487 327,487" fill="var(--olive)"/>
    <rect x="0" y="487" width="755" height="23" fill="#2b2b2b"/>
  </svg>

  <div class="landscape abs" role="img" aria-label="Photo of snowy mountains above a forest lake at sunset"></div>
  <div class="brand brand--back abs"><span class="brand__mark"></span>Meridian Hearth Realty</div>

  <p class="market-note abs">There's never been a better time to sell your home in Colorado Springs! With home values rising almost 10% in the last year alone, and predicted to jump another 3.7% within the year, it truly is a seller's market! Ready to make a change? Contact us to sell your property today!</p>

  <div class="portrait abs" role="img" aria-label="Portrait of the agent in a dark blazer"><div class="portrait__face"></div></div>
  <p class="back-tagline abs">Don't Just Tour the Town.<br>ROAM Kestrelby.</p>
  <blockquote class="review abs">“Cole is absolutely the best. Selling our home was so much easier with him as our agent. He is always there to answer questions no matter how small. I would definitely recommend him! ”<cite class="review__author">Nora</cite></blockquote>
  <p class="agent-name--back abs">Cole Barrett <b>AGENT</b></p>

  <div class="contact contact--back abs">
    <p class="contact__label">Get in touch with us</p>
    <p class="contact__phone">
      <svg width="16" height="16" viewBox="0 0 24 24" aria-hidden="true"><circle cx="12" cy="12" r="10.5" fill="none" stroke="#1c1c1c" stroke-width="2"/><path d="M8.5 6.5 L10.5 6.5 L11.3 9.3 L10 10.4 Q11 12.8 13.6 14 L14.7 12.7 L17.5 13.5 L17.5 15.5 Q17 17.5 15 17.3 Q7 16 6.7 8.5 Q6.8 6.7 8.5 6.5 Z" fill="#1c1c1c"/></svg>
      555-013-8842
    </p>
  </div>
  <div class="web web--back abs">
    <p class="web__label">For more information visit Us on :</p>
    <p class="web__url">www.roamkestrelby.example</p>
  </div>

  <div class="indicia abs">PRSRT STD<br>ECRWSS<br>U.S. POSTAGE<br><b>PAID</b><br>EDDM RETAIL</div>
  <div class="mail-panel abs">
    <p class="mail-panel__route">*****************ECRWSS****</p>
    <p>Local<br>Postal Customer</p>
  </div>
</section>

</body>
</html>
```